out of the box Business Card Design for a Manufacturer / Distributor

We are a manufarturer and distributor of products.
the company name is VORTANI (Pic attached)

the picture is NOT a must have on the business Card.

the Business Card should look really professional and/or special, so out of the box thinking is welcome.

there should be 2 Adresses on the Business Card for Main and Branch Office.
Email Adress, homepage, Name is required
NO Phone Number

Our working field:
Private Labeling
high Quality Production
direct distribution
warehousing
trademark registration
legal support

Main Office:
Kornblumenweg 14
08352 Mühlbrunn
Germany

Branch Office:
Daska Lane
Noorabad
Pakistan

Names:
Lukas Feldhaus (Owner)
Imran Qureshi (Owner)

Email:
lukas@vortani-example.com
imran@vortani-example.com

homepage:
vortani-example.com

Industry/Entity Type

Manufacturer Distributer

Contact Information for Business Card

Vortani

Requirements
Must have
• Names, both office Adresses, email, homepage
Should not have
• Phone Number

```html
<!DOCTYPE html>
<html lang="en">
<head>
<meta charset="utf-8">
<title>VORTANI Business Card</title>
<link rel="stylesheet" href="https://fonts.googleapis.com/css2?family=Mulish:wght@400;800&display=swap">
<style>
  :root {
    --bg: #e9e7e4;
    --card-dark: #4a4a4a;
    --card-light: #ffffff;
    --ink: #4a4a4a;
    --ink-soft: #5a5a5a;
    --paper-on-dark: #ffffff;
  }
  html, body {
    margin: 0;
    padding: 0;
    width: 1200px;
    height: 1200px;
    overflow: hidden;
    background: var(--bg);
    font-family: "Mulish", "Avenir Next", sans-serif;
  }
  .canvas {
    width: 1200px;
    height: 1200px;
    display: flex;
    flex-direction: column;
    align-items: center;
    justify-content: center;
    gap: 56px;
  }
  .card {
    width: 860px;
    height: 492px;
    position: relative;
    box-shadow: 0 6px 22px rgba(0,0,0,0.18);
    overflow: hidden;
  }
  .card-front {
    background: var(--card-dark);
    display: flex;
    align-items: center;
    justify-content: center;
  }
  .brand {
    display: flex;
    align-items: center;
    gap: 22px;
  }
  .brand-dot {
    width: 54px;
    height: 54px;
    border-radius: 50%;
    background: var(--paper-on-dark);
  }
  .brand-name {
    font-weight: 400;
    font-size: 72px;
    letter-spacing: 4px;
    color: var(--paper-on-dark);
  }
  .card-back {
    background: var(--card-light);
    color: var(--ink);
  }
  .card-back .brand {
    position: absolute;
    left: 64px;
    top: 56px;
    gap: 16px;
  }
  .card-back .brand-dot {
    width: 40px;
    height: 40px;
    background: var(--ink);
  }
  .card-back .brand-name {
    font-size: 50px;
    letter-spacing: 3px;
    color: var(--ink);
  }
  .person {
    position: absolute;
    left: 64px;
    top: 148px;
  }
  .person-name {
    font-weight: 800;
    font-size: 30px;
    letter-spacing: 1px;
    margin: 0;
  }
  .person-role {
    font-weight: 400;
    font-size: 28px;
    letter-spacing: 3px;
    margin: 0;
  }
  .contacts {
    position: absolute;
    left: 64px;
    top: 262px;
    display: grid;
    grid-template-columns: 30px auto;
    column-gap: 14px;
    row-gap: 4px;
    font-size: 21px;
    line-height: 30px;
    color: var(--ink-soft);
  }
  .contacts svg {
    width: 24px;
    height: 24px;
    margin-top: 3px;
    fill: var(--ink);
  }
  .contact-lines p { margin: 0; }
</style>
</head>
<body>
<main class="canvas">
  <section class="card card-front" aria-label="Business card front">
    <div class="brand">
      <span class="brand-dot"></span>
      <span class="brand-name">VORTANI</span>
    </div>
  </section>

  <section class="card card-back" aria-label="Business card back">
    <div class="brand">
      <span class="brand-dot"></span>
      <span class="brand-name">VORTANI</span>
    </div>
    <div class="person">
      <p class="person-name">LUKAS FELDHAUS</p>
      <p class="person-role">OWNER</p>
    </div>
    <div class="contacts">
      <svg viewBox="0 0 24 24" aria-hidden="true"><path d="M12 2a7 7 0 0 0-7 7c0 5 7 13 7 13s7-8 7-13a7 7 0 0 0-7-7zm0 9.5A2.5 2.5 0 1 1 12 6.5a2.5 2.5 0 0 1 0 5z"/></svg>
      <div class="contact-lines">
        <p>Kornblumenweg 14</p>
        <p>08352 Mühlbrunn Germany</p>
        <p>Daska Lane Noorabad Pakistan</p>
      </div>
      <svg viewBox="0 0 24 24" aria-hidden="true"><path d="M2 5h20v14H2z M2 5l10 8 10-8" fill="none" stroke="#4a4a4a" stroke-width="2"/><path d="M2 5h20l-10 8z"/></svg>
      <div class="contact-lines"><p>lukas@vortani-example.com</p></div>
      <svg viewBox="0 0 24 24" aria-hidden="true"><g fill="none" stroke="#4a4a4a" stroke-width="1.8"><circle cx="12" cy="12" r="9.5"/><ellipse cx="12" cy="12" rx="4" ry="9.5"/><path d="M2.5 12h19M4 7h16M4 17h16"/></g></svg>
      <div class="contact-lines"><p>vortani-example.com</p></div>
    </div>
  </section>
</main>
</body>
</html>
```